Business cards Marta Kessel Sport & Events

I need new business cards to match my new logo design for my company called "Marta Kessel Sport & Events". I'm based in Germany.
With my company, I offer different services in the context of sport.

Marta Kessel owner

Marta Kessel Sports & Events
Birkenfelder Weg 12
D-63118 Offenbach

+49 69 / 31 52 94 07
info@marta-kessel.example
www.marta-kessel.example

Contact Information for Business Card

Marta Kessel Inhaberin Marta Kessel Sport & Events Birkenfelder Weg 12 D-63118 Offenbach +49 69 / 31 52 94 07 info@marta-kessel.example www.marta-kessel.example

Requirements
Must have
• Logo | Double sided business card

```html
<!DOCTYPE html>
<html lang="de">
<head>
<meta charset="utf-8">
<title>Marta Kessel Sport &amp; Events – Visitenkarten</title>
<link href="https://fonts.googleapis.com/css2?family=Michroma&family=Roboto:wght@400;500&display=swap" rel="stylesheet">
<style>
  :root {
    --backdrop: #2b2b2b;
    --card-dark: #0e1013;
    --card-light: #ffffff;
    --accent: #f6ad33;
    --ink: #111111;
    --text-grey: #4a4a4a;
    --white: #ffffff;
  }
  * { box-sizing: border-box; margin: 0; padding: 0; }
  html, body { width: 1200px; height: 929px; overflow: hidden; }
  body {
    background: var(--backdrop);
    font-family: "Roboto", Arial, sans-serif;
    position: relative;
  }
  .card {
    position: absolute;
    left: 250px;
    width: 700px;
    height: 400px;
    border-radius: 22px;
    box-shadow: 0 12px 30px rgba(0,0,0,.45);
    overflow: hidden;
  }
  .card--front { top: 44px; background: var(--card-dark); }
  .card--back  { top: 485px; background: var(--card-light); }

  .wordmark {
    position: absolute;
    display: flex;
    align-items: center;
    gap: 18px;
    font-family: "Michroma", "Arial Black", sans-serif;
    text-transform: uppercase;
    line-height: 1.35;
  }
  .wordmark__dot {
    width: 74px; height: 74px; border-radius: 50%;
    background: var(--accent); flex: none;
  }
  .wordmark__name { display: block; }
  .card--front .wordmark {
    left: 50%; top: 50%; transform: translate(-50%, -50%);
    color: var(--accent); font-size: 26px;
  }
  .card--back .wordmark {
    right: 48px; top: 58px; color: var(--accent); font-size: 17px; gap: 14px;
  }
  .card--back .wordmark__dot { width: 54px; height: 54px; }

  .holder {
    position: absolute; left: 60px; top: 150px;
  }
  .holder__name {
    font-family: "Michroma", "Arial Black", sans-serif;
    font-size: 20px; color: var(--ink); text-transform: uppercase;
    letter-spacing: .5px;
  }
  .holder__role {
    display: flex; align-items: center; gap: 10px;
    color: var(--accent); font-size: 18px; font-weight: 500; margin-top: 4px;
  }
  .rule {
    height: 1.5px; background: var(--accent); width: 500px;
  }
  .contacts {
    position: absolute; left: 78px; top: 240px;
    list-style: none; color: var(--text-grey); font-size: 17px; line-height: 30px;
  }
  .contacts li { display: flex; align-items: center; gap: 10px; }
  .contacts svg { width: 16px; height: 16px; fill: var(--accent); flex: none; }
  .address {
    position: absolute; right: 48px; top: 232px;
    text-align: right; font-style: normal;
    color: var(--text-grey); font-size: 17px; line-height: 26px;
  }
</style>
</head>
<body>
  <section class="card card--front" aria-label="Vorderseite">
    <div class="wordmark">
      <span class="wordmark__dot"></span>
      <span class="wordmark__name">Marta Kessel<br>Sport &amp; Events</span>
    </div>
  </section>

  <section class="card card--back" aria-label="Rückseite">
    <div class="wordmark">
      <span class="wordmark__dot"></span>
      <span class="wordmark__name">Marta Kessel<br>Sport &amp; Events</span>
    </div>

    <div class="holder">
      <h1 class="holder__name">Marta Kessel</h1>
      <p class="holder__role">Owner <span class="rule"></span></p>
    </div>

    <ul class="contacts">
      <li>
        <svg viewBox="0 0 16 16" aria-hidden="true"><path d="M3 1l3 3-1.5 2a9 9 0 0 0 5.5 5.5L12 10l3 3-2 2C7 15 1 9 1 3z"/></svg>
        +49 69 / 31 52 94 07
      </li>
      <li>
        <svg viewBox="0 0 16 16" aria-hidden="true"><path d="M1 3h14v10H1z M2 4l6 5 6-5" stroke="#fff" stroke-width="1.2"/></svg>
        info@marta-kessel.example
      </li>
      <li>
        <svg viewBox="0 0 16 16" aria-hidden="true"><circle cx="8" cy="8" r="7"/><path d="M1 8h14M8 1c-3 4-3 10 0 14M8 1c3 4 3 10 0 14" stroke="#fff" stroke-width="1" fill="none"/></svg>
        www.marta-kessel.example
      </li>
    </ul>

    <address class="address">
      Marta Kessel Sport &amp; Events<br>
      Birkenfelder Weg 12<br>
      D-63118 Offenbach
    </address>
  </section>
</body>
</html>
```